updated documents

Hi i have included a new picture for the about us section, i have also included the updated word document, all changes have been highlighted.

Thanks,

Tobin

```html
<!DOCTYPE html>
<html lang="en">
<head>
<meta charset="utf-8">
<title>Keystone Property Services – Business Brochure</title>
<link href="https://fonts.googleapis.com/css2?family=Cinzel:wght@400;600&family=Crimson+Text:wght@400;600&family=Open+Sans:wght@400&display=swap" rel="stylesheet">
<style>
:root{
  --stage:#1f1f1f;
  --paper:#ffffff;
  --green:#a9cb37;
  --grey:#6b6c6e;
  --ink:#3a3a3a;
  --body:#555555;
  --photo-a:#c9d2d8;
  --photo-b:#8e9aa3;
}
*{margin:0;padding:0;box-sizing:border-box}
html,body{width:1200px;height:960px;overflow:hidden;background:var(--stage)}
.board{position:relative;width:1200px;height:960px}
.page-label{position:absolute;width:160px;margin-left:-80px;text-align:center;font:400 10.5px/1 "Open Sans",sans-serif;color:#e6e6e6}
.spread{position:absolute;width:518px;height:366px;overflow:hidden;background:var(--paper)}
.spread-inner{position:absolute;left:0;top:0;width:647px;height:458px;transform:scale(.8);transform-origin:0 0}
.spread-inner svg.art{position:absolute;left:0;top:0;width:647px;height:458px}
.txt{position:absolute}
.section-title{font:400 22px/1 "Cinzel",serif;color:var(--green);letter-spacing:.5px}
.item-title{font:600 9.5px/1.35 "Cinzel",serif;color:var(--ink);text-transform:uppercase;letter-spacing:.3px}
.body-copy{font:400 8px/11.7px "Crimson Text",serif;color:var(--body)}
.body-copy.set-lines{white-space:nowrap}
.item-icon{position:absolute;width:17px;height:17px;background:var(--green);border-radius:3px}
.brand-name{font:400 13px/1 "Cinzel",serif;color:var(--ink);letter-spacing:.6px;white-space:nowrap}
.brand-mark{position:absolute;width:26px;height:26px;background:var(--green)}
.cover-title{font:400 29px/1.08 "Cinzel",serif;letter-spacing:1px}
.cover-title .l1{color:var(--grey);display:block}
.cover-title .l2{color:var(--green);display:block}
.contact-title{font:400 14px/1 "Cinzel",serif;color:var(--ink)}
.contact-list{list-style:none;font:400 9px/1 "Crimson Text",serif;color:var(--ink)}
.contact-list li{display:flex;align-items:center;gap:4px;height:17.5px}
.contact-list svg{width:11px;height:11px;flex:none}
.site-url{font:400 8.5px/1 "Crimson Text",serif;color:var(--ink)}
</style>
</head>
<body>
<main class="board">

  <span class="page-label" style="left:186px;top:48px">Back Page</span>
  <span class="page-label" style="left:446px;top:48px">Cover Page</span>
  <span class="page-label" style="left:758px;top:48px">Page 1</span>
  <span class="page-label" style="left:1018px;top:48px">Page 2</span>
  <span class="page-label" style="left:186px;top:522px">Page 3</span>
  <span class="page-label" style="left:446px;top:522px">Page 4</span>
  <span class="page-label" style="left:745px;top:522px">Page 5</span>
  <span class="page-label" style="left:1005px;top:522px">Page 6</span>

  <!-- Back page + cover -->
  <section class="spread spread-cover" style="left:65px;top:71px">
    <div class="spread-inner">
      <svg class="art" viewBox="0 0 647 458">
        <defs>
          <linearGradient id="gPhoto" x1="0" y1="0" x2="1" y2="1">
            <stop offset="0" stop-color="var(--photo-a)"/><stop offset="1" stop-color="var(--photo-b)"/>
          </linearGradient>
          <linearGradient id="gHands" x1="0" y1="0" x2="1" y2="1">
            <stop offset="0" stop-color="#dde7ef"/><stop offset="1" stop-color="#9fb0bf"/>
          </linearGradient>
        </defs>
        <polygon points="0,0 205,0 60,150 0,90" fill="url(#gHands)" role="img" aria-label="Photo of a business handshake"/>
        <polygon points="0,100 60,165 222,0 338,0 74,268 0,196" fill="var(--green)"/>
        <polygon points="0,215 58,275 0,335 0,305 28,275 0,245" fill="var(--grey)"/>
        <polygon points="165,240 350,48 647,345 647,410 350,110 228,240" fill="var(--grey)"/>
        <polygon points="165,245 228,245 330,362 575,142 645,142 330,432" fill="var(--green)"/>
        <polygon points="355,124 468,238 355,352 242,238" fill="#ffffff"/>
        <polygon points="355,134 458,238 355,342 252,238" fill="url(#gPhoto)" role="img" aria-label="Photo of a bright modern office interior"/>
      </svg>

      <div class="brand-mark" style="left:528px;top:40px"></div>
      <div class="txt brand-name" style="left:444px;top:82px">Keystone Property Services</div>

      <h1 class="txt cover-title" style="left:439px;top:368px"><span class="l1">Business</span><span class="l2">Brochure</span></h1>

      <div class="txt" style="left:20px;top:343px">
        <h2 class="contact-title">Contact Us</h2>
        <ul class="contact-list" style="margin-top:8px">
          <li><svg viewBox="0 0 12 12"><circle cx="6" cy="6" r="5.3" fill="none" stroke="#444" stroke-width="1"/><path d="M4 3.5l1 1.2-.6.8c.5 1 1.1 1.6 2 2l.8-.6 1.2 1-.6 1C6 8.7 3.3 6 3.4 4.1z" fill="#444"/></svg>0400 123 456</li>
          <li><svg viewBox="0 0 12 12"><circle cx="6" cy="6" r="5.3" fill="none" stroke="#444" stroke-width="1"/><rect x="3.3" y="4.2" width="5.4" height="3.6" fill="none" stroke="#444" stroke-width=".8"/><path d="M3.3 4.2L6 6.3l2.7-2.1" fill="none" stroke="#444" stroke-width=".8"/></svg>adam.tobin@keystoneps.com.au</li>
          <li><svg viewBox="0 0 12 12"><circle cx="6" cy="6" r="5.3" fill="none" stroke="#444" stroke-width="1"/><circle cx="6" cy="6" r="3" fill="none" stroke="#444" stroke-width=".8"/><path d="M3 6h6M6 3v6" stroke="#444" stroke-width=".6"/></svg>www.keystonepropertyservices.com</li>
          <li><svg viewBox="0 0 12 12"><circle cx="6" cy="6" r="5.3" fill="none" stroke="#444" stroke-width="1"/></svg>www.social.com/keystoneproperty</li>
        </ul>
      </div>
    </div>
  </section>

  <!-- Pages 1 and 2 -->
  <section class="spread spread-about" style="left:638px;top:71px">
    <div class="spread-inner">
      <svg class="art" viewBox="0 0 647 458">
        <defs>
          <linearGradient id="gTeam" x1="0" y1="0" x2="0" y2="1">
            <stop offset="0" stop-color="#e9edf1"/><stop offset="1" stop-color="#aab4bd"/>
          </linearGradient>
          <linearGradient id="gPaint" x1="0" y1="0" x2="1" y2="1">
            <stop offset="0" stop-color="#eef0ee"/><stop offset="1" stop-color="#c9cdcc"/>
          </linearGradient>
          <linearGradient id="gElec" x1="0" y1="0" x2="1" y2="1">
            <stop offset="0" stop-color="#b7c2cc"/><stop offset="1" stop-color="#4e5f70"/>
          </linearGradient>
        </defs>
        <rect x="15" y="40" width="290" height="170" fill="url(#gTeam)" role="img" aria-label="Photo of the trades team standing in work clothes and helmets"/>
        <polygon points="333,0 403,0 578,185 647,116 647,186 578,260" fill="var(--grey)"/>
        <polygon points="403,0 647,0 647,116 578,185" fill="var(--green)"/>
        <polygon points="425,6 641,6 641,114 578,176" fill="url(#gPaint)" role="img" aria-label="Photo of painters rolling paint onto a wall"/>
        <polygon points="150,458 315,280 500,458" fill="var(--green)"/>
        <polygon points="210,458 320,338 432,458" fill="#ffffff"/>
        <polygon points="222,458 320,352 420,458" fill="url(#gElec)" role="img" aria-label="Photo of an electrician working on a switchboard"/>
      </svg>

      <h2 class="txt section-title" style="left:16px;top:228px">About Us</h2>
      <p class="txt body-copy set-lines" style="left:17px;top:260px">Keystone Property Services is an Adelaide based company providing general building<br>and office maintenance and refurbishments. We pride ourselves in delivering cost<br>affective high quality services with minimal disturbance to tenants and their<br>occupants.</p>
      <p class="txt body-copy set-lines" style="left:17px;top:318px">Keystone Property Services provides a wide range of services including<br>all major trades Electrical, Data, Plumbing, carpentry, landscaping,<br>and more. With all trades available we can manage their work as<br>required. We also provide preventive maintenance programs<br>to help reduce future reactive works. Our Team are have<br>all undertaken police checks and are white card<br>accredited.</p>
      <p class="txt site-url" style="left:17px;top:434px">keystonepropertyservices.com</p>

      <h2 class="txt section-title" style="left:335px;top:136px">Services</h2>
      <span class="item-icon" style="left:338px;top:172px"></span>
      <h3 class="txt item-title" style="left:375px;top:174px">Building Repairs<br>&amp; Maintenance</h3>
      <p class="txt body-copy set-lines" style="left:337px;top:209px">The team at Keystone Property Services have extensive<br>skills and experience in both internal and external build-<br>ing repairs and maintenance. Installation and repairs to floor<br>and ceilings systems, doors/locks, appliance repairs, whiteboards,<br>TV screens, picture hanging, patching and paint, vandal repairs,<br>workstations and joinery, plumbing and electrical.</p>
      <span class="item-icon" style="left:462px;top:306px"></span>
      <h3 class="txt item-title" style="left:497px;top:312px">Electrical</h3>
      <p class="txt body-copy" style="left:462px;top:333px;width:178px">Keystone Property Services provides a wide range of electrical services ranging from Test and tag, Mains services, Switchboard installations, fault finding, RCD testing, data cabling/patching, electrical upgrades and lighting.</p>
    </div>
  </section>

  <!-- Pages 3 and 4 -->
  <section class="spread spread-services-a" style="left:65px;top:546px">
    <div class="spread-inner">
      <svg class="art" viewBox="0 0 647 458">
        <defs>
          <linearGradient id="gCeil" x1="0" y1="0" x2="1" y2="1">
            <stop offset="0" stop-color="#d9d6cf"/><stop offset="1" stop-color="#8b8f93"/>
          </linearGradient>
          <linearGradient id="gClean" x1="0" y1="0" x2="1" y2="1">
            <stop offset="0" stop-color="#c7ccd3"/><stop offset="1" stop-color="#6d7782"/>
          </linearGradient>
        </defs>
        <polygon points="0,0 200,0 60,148 0,88" fill="url(#gCeil)" role="img" aria-label="Photo of a worker on a ladder fixing a ceiling"/>
        <polygon points="0,100 60,162 215,0 262,0 60,215 0,155" fill="var(--green)"/>
        <polygon points="125,458 350,218 590,458" fill="var(--grey)"/>
        <polygon points="215,458 350,290 485,458" fill="#ffffff"/>
        <polygon points="228,458 350,305 472,458" fill="url(#gClean)" role="img" aria-label="Photo of an office floor being mopped beside a wet floor sign"/>
        <polygon points="647,262 533,375 620,458 647,458 647,432 590,375 647,318" fill="var(--green)"/>
      </svg>

      <span class="item-icon" style="left:205px;top:66px"></span>
      <h3 class="txt item-title" style="left:228px;top:71px">Planned<br>Preventative<br>Maintenance</h3>
      <p class="txt body-copy" style="left:157px;top:122px;width:162px">Keystone Property Services Offer planned preventive maintenance specifically tailored to the client's requirements. Planned maintenance schedules can be created to prevent break-downs and costly reactive maintenance in the future. Maintenance programs can include floor and ceiling repairs, light bulb replacements, Test and tagging, Storm water and gutter cleaning.</p>

      <span class="item-icon" style="left:17px;top:250px"></span>
      <h3 class="txt item-title" style="left:37px;top:259px">Painting</h3>
      <p class="txt body-copy" style="left:17px;top:277px;width:182px">Keystone Property Services pride ourselves in quality and detail ensuring the very best results while being a cost effective and efficient.</p>
      <span class="item-icon" style="left:17px;top:328px"></span>
      <h3 class="txt item-title" style="left:44px;top:338px">Signage</h3>
      <p class="txt body-copy" style="left:17px;top:355px;width:182px">Keystone Property Services have an experience signage team that specialize in both internal and external signage, decals, promotional banners, window frosting, company logos and design.</p>

      <span class="item-icon" style="left:345px;top:34px"></span>
      <h3 class="txt item-title" style="left:373px;top:40px">Office Layout Changes</h3>
      <p class="txt body-copy" style="left:347px;top:58px;width:282px">If you are looking to make some changes to your office either big or small our team can assist with Workstation reconfiguration, internal demolition, Partition/wall installations and even complete office relocations.</p>
      <span class="item-icon" style="left:345px;top:128px"></span>
      <h3 class="txt item-title" style="left:373px;top:134px">Appliance Repairs</h3>
      <p class="txt body-copy" style="left:345px;top:151px;width:288px">Keystone Property Services can repair and replace all of your office appliance's ranging from dishwashers and microwaves to monitors, TV's and projectors.</p>
      <span class="item-icon" style="left:431px;top:204px"></span>
      <h3 class="txt item-title" style="left:457px;top:213px">Cleaning</h3>
      <p class="txt body-copy" style="left:430px;top:230px;width:200px">Our team offer both internal and external cleaning services including carpark cleaning, window cleaning, carpet dry cleaning, and general office cleaning.</p>
    </div>
  </section>

  <!-- Pages 5 and 6 -->
  <section class="spread spread-services-b" style="left:624px;top:546px">
    <div class="spread-inner">
      <svg class="art" viewBox="0 0 647 458">
        <defs>
          <linearGradient id="gPlumb" x1="0" y1="0" x2="1" y2="1">
            <stop offset="0" stop-color="#e4e7ea"/><stop offset="1" stop-color="#5f6f8c"/>
          </linearGradient>
          <linearGradient id="gCarp" x1="0" y1="0" x2="1" y2="1">
            <stop offset="0" stop-color="#d8cdb8"/><stop offset="1" stop-color="#8a7a62"/>
          </linearGradient>
        </defs>
        <polygon points="0,10 85,95 0,180 0,140 45,95 0,50" fill="var(--green)"/>
        <polygon points="15,0 88,0 255,170 365,0 440,0 255,240" fill="var(--grey)"/>
        <polygon points="98,0 358,0 255,155" fill="url(#gPlumb)" role="img" aria-label="Photo of a plumber fixing pipes under a sink"/>
        <polygon points="0,458 78,378 125,378 45,458" fill="var(--green)"/>
        <polygon points="70,458 150,368 240,458 198,458 150,408 112,458" fill="var(--grey)"/>
        <polygon points="300,458 380,378 430,378 350,458" fill="var(--grey)"/>
        <polygon points="458,458 582,252 647,296 647,458" fill="var(--green)"/>
        <polygon points="505,458 598,330 647,362 647,458" fill="url(#gCarp)" role="img" aria-label="Photo of a carpenter cutting timber with a circular saw"/>
      </svg>

      <span class="item-icon" style="left:15px;top:170px"></span>
      <h3 class="txt item-title" style="left:40px;top:170px">Rubbish Removal<br>/Recycling</h3>
      <p class="txt body-copy" style="left:15px;top:201px;width:190px">If you are looking to make some changes to your office either big or small our team can assist with Workstation reconfiguration, internal demolition, Partition/wall installations and even complete office relocations.</p>
      <span class="item-icon" style="left:15px;top:280px"></span>
      <h3 class="txt item-title" style="left:37px;top:291px">Plumbing</h3>
      <p class="txt body-copy" style="left:15px;top:310px;width:290px">Our Plumbing team are experienced and available 24/7 for all your plumbing requirements. Our plumbing services include, water boiler/chiller unit installs and repairs, blocked drains and toilets, roof work and gas fitting.</p>

      <span class="item-icon" style="left:465px;top:47px"></span>
      <h3 class="txt item-title" style="left:497px;top:50px">Grounds Keeping</h3>
      <p class="txt body-copy" style="left:466px;top:72px;width:178px">Let us help with your grounds keeping, our services include, lawn mowing and garden care, carpark sweeping, tree pruning, line marking, gutter cleaning, landscaping, bird and pest management, fencing installs and repairs.</p>
      <span class="item-icon" style="left:362px;top:161px"></span>
      <h3 class="txt item-title" style="left:388px;top:168px">Carpentry</h3>
      <p class="txt body-copy" style="left:361px;top:186px;width:270px">Keystone Property Services have a dedicated carpentry team that can assist with all your requirements including Partitioning, cupboard installations and all repairs and modifications.</p>
      <span class="item-icon" style="left:338px;top:254px"></span>
      <h3 class="txt item-title" style="left:378px;top:268px">Floor /Ceiling</h3>
      <p class="txt body-copy" style="left:335px;top:286px;width:180px">We can provide floor and ceiling repairs to all types of systems including, suspended ceiling systems and raised floors, ceiling/floor tile replacement, carpet and vinyl replacements and repairs, ceiling access hatches and air vent installs.</p>
    </div>
  </section>

</main>
</body>
</html>
```